Construction Directory Website Flyer

We need a postcard size +/- or somewhere around that size (something standard) flyer designed for our construction directory website. Leave a spot for tagline. Call to action is 'register your company now'. I am thinking many mini pictures of different construction to show that it is for the entire construction industry. Logo and screenshot of the homepage of the website is attached. Use same theme as webpage.

Target Market(s)

Construction Industry

Industry/Entity Type

Construction

Font styles to use
Sans Serif

Requirements
Must have
• Call to action
• Colors to match logo
• Area to add description and details.
Nice to have
• Construction Images
Should not have
• No Cartoonish types of things

```html
<!DOCTYPE html>
<html lang="en">
<head>
<meta charset="utf-8">
<title>BuildLink Directory Flyer</title>
<link rel="stylesheet" href="https://fonts.googleapis.com/css2?family=Lato:wght@400;700;900&family=Oswald:wght@700&display=swap">
<style>
  :root {
    --brand-orange: #e04b26;
    --ink: #161616;
    --slate: #3d4248;
    --paper: #ffffff;
    --stage: #ecebe8;
    --skyline-light: #f1f1f1;
    --skyline-mid: #d6d6d6;
    --sky-blue: #8fb9dc;
    --concrete: #b9b3a6;
    --asphalt: #2b2d30;
  }
  * { box-sizing: border-box; margin: 0; padding: 0; }
  html, body {
    width: 1200px; height: 1200px; overflow: hidden;
    background: var(--stage);
  }
  .flyer {
    position: absolute; left: 30px; top: 140px;
    width: 1140px; height: 920px;
    background: var(--paper);
    overflow: hidden;
    box-shadow: 0 10px 30px rgba(0,0,0,0.18);
    font-family: "Lato", Arial, sans-serif;
  }
  .flyer-shapes { position: absolute; inset: 0; }
  .brand {
    position: absolute; left: 728px; top: 82px;
    display: flex; align-items: center; gap: 18px;
  }
  .brand-mark {
    width: 74px; height: 74px; background: var(--brand-orange);
  }
  .brand-name {
    font-family: "Lato", Arial, sans-serif;
    font-weight: 400; font-size: 48px; line-height: 46px;
    color: var(--slate); letter-spacing: 1px;
  }
  .tagline {
    position: absolute; left: 42px; top: 418px;
    font-weight: 900; line-height: 1;
  }
  .tagline-lead { display: block; font-size: 80px; color: var(--paper); letter-spacing: -1px; }
  .tagline-mid { display: block; font-size: 48px; color: var(--paper); margin-top: 6px; }
  .tagline-end { display: block; font-size: 44px; color: var(--ink); margin-top: 8px; }
  .contact {
    position: absolute; left: 42px; top: 728px;
    color: var(--ink); font-weight: 700;
  }
  .contact-line { display: flex; align-items: center; gap: 10px; }
  .contact-phone { font-size: 28px; font-weight: 900; }
  .contact-email { font-size: 16px; margin-top: 14px; }
  .contact svg { flex: none; }
  .cta {
    position: absolute; right: 58px; top: 690px; text-align: right;
  }
  .cta-main {
    display: block;
    font-family: "Oswald", "Arial Narrow", sans-serif;
    font-weight: 700; font-size: 118px; line-height: 1;
    color: var(--brand-orange); letter-spacing: -1px;
  }
  .cta-sub {
    display: block; margin-top: 2px;
    font-weight: 900; font-size: 37px; color: var(--ink);
  }
</style>
</head>
<body>
<main class="flyer">
  <svg class="flyer-shapes" width="1140" height="920" viewBox="0 0 1140 920">
    <defs>
      <linearGradient id="skylineTone" x1="0" y1="0" x2="1" y2="1">
        <stop offset="0" stop-color="var(--skyline-light)"/>
        <stop offset="1" stop-color="var(--skyline-mid)"/>
      </linearGradient>
      <linearGradient id="bridgeTone" x1="0" y1="0" x2="0" y2="1">
        <stop offset="0" stop-color="var(--sky-blue)"/>
        <stop offset="1" stop-color="var(--concrete)"/>
      </linearGradient>
      <linearGradient id="pavingTone" x1="0" y1="0" x2="0" y2="1">
        <stop offset="0" stop-color="#6f8f4e"/>
        <stop offset="0.35" stop-color="#3b3b3b"/>
        <stop offset="1" stop-color="var(--asphalt)"/>
      </linearGradient>
      <filter id="edgeShadow" x="-10%" y="-10%" width="120%" height="120%">
        <feDropShadow dx="6" dy="4" stdDeviation="6" flood-color="#000" flood-opacity="0.25"/>
      </filter>
    </defs>

    <polygon class="skyline-photo" role="img" aria-label="Faded photo of high-rise buildings under construction with tower cranes"
             points="104,0 1140,0 1140,290 760,672 557,460" fill="url(#skylineTone)"/>

    <polygon class="brand-panel" points="0,0 104,0 557,460 225,920 0,920"
             fill="var(--brand-orange)" filter="url(#edgeShadow)"/>

    <polygon class="photo-tile bridge" role="img" aria-label="Photo of a concrete highway overpass under construction against blue sky"
             points="469,148 647,331 469,514 291,331" fill="url(#bridgeTone)"
             stroke="var(--ink)" stroke-width="2" filter="url(#edgeShadow)"/>
    <polygon class="photo-tile paving" role="img" aria-label="Photo of road workers in orange hi-vis spreading fresh asphalt with a rake"
             points="682,351 859,534 682,717 505,534" fill="url(#pavingTone)"
             stroke="var(--ink)" stroke-width="2" filter="url(#edgeShadow)"/>
  </svg>

  <div class="brand">
    <span class="brand-mark"></span>
    <span class="brand-name">BuildLink<br>Directory</span>
  </div>

  <h1 class="tagline">
    <span class="tagline-lead">Built by</span>
    <span class="tagline-mid">Construction</span>
    <span class="tagline-end">for Construction</span>
  </h1>

  <div class="contact">
    <div class="contact-line contact-phone">
      <svg width="28" height="28" viewBox="0 0 24 24" aria-hidden="true"><path fill="var(--ink)" d="M6.6 10.8c1.4 2.8 3.8 5.1 6.6 6.6l2.2-2.2c.3-.3.7-.4 1-.2 1.1.4 2.3.6 3.6.6.6 0 1 .4 1 1V20c0 .6-.4 1-1 1C10.6 21 3 13.4 3 4c0-.6.4-1 1-1h3.5c.6 0 1 .4 1 1 0 1.3.2 2.5.6 3.6.1.3 0 .7-.2 1z"/></svg>
      <span>014-555-0192</span>
    </div>
    <div class="contact-line contact-email">
      <svg width="28" height="24" viewBox="0 0 28 24" aria-hidden="true"><g fill="none" stroke="var(--ink)" stroke-width="1.6"><rect x="1" y="8" width="26" height="15"/><path d="M1 8l13 9 13-9M1 23l10-8M27 23l-10-8"/><path d="M8 11V1h12v10M11 4h6M11 7h6"/></g></svg>
      <span>info@buildlinkdirectory.com</span>
    </div>
  </div>

  <div class="cta">
    <span class="cta-main">Register</span>
    <span class="cta-sub">your company now</span>
  </div>
</main>
</body>
</html>
```